Innovative mission-driven diversity services company needs launch brochure

Two-sided 8 1/5" x 11" document to demonstrate a new program.

Target Market(s)

Chief Diversity Officers and Hiring Managers at advertising/communications agencies who are looking to attract and hire recently graduated/about to graduate African American students

Industry/Entity Type

It Company

Requirements
Must have
• a very contemporary feel that will well represent the vibrancy, energy, and identity of the African American student population. This is a cause driven organization and that passion and purpose should be conveyed while recognizing that the target audience are corporate executives.

```html
<!DOCTYPE html>
<html lang="en">
<head>
<meta charset="utf-8">
<title>Tenfold LLC – Narrowing the Racial Diversity Gap</title>
<link rel="stylesheet" href="https://fonts.googleapis.com/css2?family=Montserrat:wght@600;700;800&family=Arimo:wght@400;700&family=Oswald:wght@600&family=Lora:ital@1&display=swap">
<style>
:root{
  --blue:#1565c0;
  --blue-deep:#0d4fa3;
  --blue-light:#2f86d8;
  --yellow:#ffd200;
  --orange:#f39200;
  --ink:#222;
  --grey:#555;
  --grey-light:#8a8a8a;
  --panel:#f6f6f6;
  --rule:#d9d9d9;
  --stage:#ebe8e3;
}
*{margin:0;padding:0;box-sizing:border-box}
html,body{width:1200px;height:944px;overflow:hidden;background:var(--stage)}
body{position:relative;font-family:"Arimo",Arial,sans-serif;color:var(--ink)}
.page{position:absolute;top:68px;width:650px;height:920px;background:#fff;transform:scale(.877);transform-origin:top left;overflow:hidden}
.page--front{left:20px}
.page--back{left:610px}
.abs{position:absolute}

/* front */
.hero{position:absolute;left:0;top:0;width:650px;height:375px;background:linear-gradient(135deg,var(--blue-light) 0%,var(--blue) 45%,var(--blue-deep) 100%)}
.brand-name{left:48px;top:36px;width:250px;font:800 52px/1 "Montserrat",sans-serif;color:#fff}
.hero-title{left:311px;top:28px;font:700 29px/1.07 "Montserrat",sans-serif;color:#fff}
.hero-sub{left:311px;top:97px;width:270px;font:700 11.5px/1.3 "Montserrat",sans-serif;color:var(--yellow)}
.hero-rule{left:60px;top:155px;width:532px;height:1px;background:rgba(255,255,255,.45)}
.hero-intro{left:60px;top:168px;width:532px;text-align:center;font-size:12.4px;line-height:1.33;color:#fff}

.chart{left:45px;top:217px;width:562px;height:248px;background:#fff}
.chart-title{position:absolute;left:0;top:15px;width:100%;text-align:center;font:700 14px "Arimo",sans-serif;color:var(--blue);letter-spacing:.2px}
.chart svg{position:absolute;left:0;top:0}

.body-copy{left:45px;top:476px;width:565px;font-size:10.8px;line-height:1.35;color:#333}
.body-copy p+p{margin-top:3px}
.section-head{left:0;width:650px;text-align:center;font:600 17.5px/1 "Oswald",sans-serif;color:#1b1b1b;letter-spacing:-.2px;transform:scaleX(.92)}

.card{position:absolute;top:587px;height:114px;border:1px solid var(--rule);background:#fff}
.card--article{left:47px;width:228px;padding:6px 13px}
.card-kicker{font:700 6px "Arimo",sans-serif;color:#999;letter-spacing:.3px}
.card-headline{margin-top:6px;font:700 16px/1.1 "Arimo",sans-serif;color:#222;letter-spacing:-.3px}
.share-row{display:flex;gap:2px;margin-top:5px}
.share-row span{display:block;width:13px;height:8px;background:#3b5998}
.share-row span:nth-child(2){background:#1da1f2}
.share-row span:nth-child(3){background:#e4572e}
.card-byline{margin-top:7px;font-size:5.5px;color:#999}
.card--quote{left:287px;width:325px}
.portrait{position:absolute;left:10px;top:10px;width:88px;height:88px;border-radius:50%;background:radial-gradient(circle at 50% 45%,#c9b2a3,#6d5a50)}
.quote-text{position:absolute;left:110px;top:9px;width:205px;font:italic 10.6px/1.35 "Lora",serif;color:#333}
.quote-name{position:absolute;left:108px;top:73px;font:700 11px "Arimo",sans-serif;color:#222}
.quote-role{position:absolute;left:108px;top:87px;font:700 8.5px "Arimo",sans-serif;color:#333}

.reason{position:absolute;top:770px;width:165px}
.reason-image{height:70px}
.reason-caption{margin-top:7px;font-size:10.2px;line-height:1.35;color:#666}
.reason--1{left:48px}.reason--2{left:248px}.reason--3{left:450px}
.reason--1 .reason-image{background:linear-gradient(135deg,#b33b3b,#4a3a3a 60%,#222)}
.reason--2 .reason-image{background:linear-gradient(90deg,#e9c9a8,#d9533a 50%,#f1e3cf)}
.reason--3 .reason-image{background:linear-gradient(180deg,#f3f3f3,#d8d8d8)}
.foot-band{left:0;top:912px;width:650px;height:8px;background:var(--blue)}

/* back */
.mission-title{left:28px;top:36px;font:700 38px/1 "Montserrat",sans-serif;color:var(--blue)}
.mission-rule{left:0;top:87px;width:430px;height:1px;background:var(--rule)}
.mission-text{left:31px;top:99px;width:590px;font:700 12.6px/1.45 "Arimo",sans-serif;color:#111}
.flow{position:absolute;left:0;top:0}
.step{position:absolute;background:var(--panel);border:1px solid #e6e6e6;border-radius:4px;padding:12px 11px}
.step h3{font:700 13px/1.2 "Montserrat",sans-serif;color:var(--blue)}
.step p{font-size:9.8px;line-height:1.34;color:#333}
.step--connect{left:35px;top:213px;width:130px;height:165px}
.step--vetting{left:179px;top:213px;width:135px;height:183px}
.step--training{left:331px;top:213px;width:263px;height:218px}
.step--onboard{left:35px;top:506px;width:253px;height:108px}
.step--building{left:308px;top:506px;width:309px;height:108px}
.step h3+p{margin-top:15px}
.training-cols{display:flex;gap:14px;margin-top:20px}
.training-cols p:first-child{width:82px;flex:none}

.about{left:0;top:632px;width:650px;height:288px;background:linear-gradient(135deg,var(--blue-light) 0%,var(--blue) 45%,var(--blue-deep) 100%)}
.about-title{left:42px;top:26px;font:800 32px/1 "Montserrat",sans-serif;color:var(--yellow)}
.about-rule{left:0;top:72px;width:428px;height:1px;background:rgba(255,255,255,.5)}
.about-copy{left:42px;top:82px;width:568px;font-size:10.9px;line-height:1.47;color:#fff}
.about-copy p+p{margin-top:11px}
</style>
</head>
<body>

<section class="page page--front">
  <div class="hero"></div>
  <div class="abs brand-name">Tenfold LLC</div>
  <h1 class="abs hero-title">Narrowing the<br>Racial Diversity Gap</h1>
  <p class="abs hero-sub">A powerful new approach to increasing the African-American employment rate in the communications industry</p>
  <div class="abs hero-rule"></div>
  <p class="abs hero-intro">Despite efforts to increase participation, African-American rates of employment in the communications industry have actually declined over the past decade</p>

  <div class="abs chart">
    <h2 class="chart-title">AFRICAN-AMERICAN PROPORTION OF WORKFORCE*</h2>
    <svg width="562" height="248" viewBox="0 0 562 248" font-family="Arimo, Arial, sans-serif">
      <text x="148" y="60" font-size="15" fill="#333" text-anchor="middle">2015</text>
      <text x="415" y="60" font-size="15" fill="#333" text-anchor="middle">2016</text>
      <g fill="#f39200">
        <rect x="48" y="81" width="72" height="101"/>
        <rect x="160" y="120" width="72" height="62"/>
        <rect x="315" y="68" width="73" height="114"/>
        <rect x="427" y="137" width="73" height="45"/>
      </g>
      <g fill="#fff" font-family="Oswald, sans-serif" font-weight="600" font-size="18" text-anchor="middle">
        <text x="84" y="168">11%</text><text x="196" y="168">7%</text>
        <text x="351" y="168">12%</text><text x="463" y="168">5%</text>
      </g>
      <line x1="30" y1="182" x2="518" y2="182" stroke="#bbb" stroke-width="1"/>
      <g fill="#444" font-size="8.6" text-anchor="middle" letter-spacing=".3">
        <text x="84" y="200">OVERALL</text><text x="84" y="212">WORKFORCE</text>
        <text x="196" y="200">COMMUNICATIONS</text><text x="196" y="212">INDUSTRY</text>
        <text x="351" y="200">OVERALL</text><text x="351" y="212">WORKFORCE</text>
        <text x="463" y="200">COMMUNICATIONS</text><text x="463" y="212">INDUSTRY</text>
      </g>
    </svg>
  </div>

  <div class="abs body-copy">
    <p>While the communications agency hiring rate of people of Hispanic or Asian origin has reached parity with their overall workforce participation rates, African-American participation has actually dropped by nearly a third.</p>
    <p>Communications agencies have identified this gap as a critical issue but are falling further behind on AA hiring.<br>*REFERENCE TO COME</p>
  </div>

  <h2 class="abs section-head" style="top:556px">CLIENTS HAVE NOW BEGUN TO DIRECTLY EXERT PRESSURE ON THE INDUSTRY</h2>

  <article class="card card--article">
    <div class="card-kicker">BRANDS</div>
    <h3 class="card-headline">Harvest Foods Insists That Its Future Agencies Meet Specific Diversity Quotas</h3>
    <div class="share-row"><span></span><span></span><span></span></div>
    <div class="card-byline">By Evan Ross on Aug. 31, 2018 – 11:06 AM</div>
  </article>

  <figure class="card card--quote">
    <div class="portrait" role="img" aria-label="Portrait photo of Dana Whitfield"></div>
    <blockquote class="quote-text">“In order to push yourself to have a more diverse work force you have to be intentional about it — and nothing will drive intent faster than a client’s dollar”</blockquote>
    <figcaption>
      <div class="quote-name">Dana Whitfield</div>
      <div class="quote-role">President &amp; CEO, Agency Alliance</div>
    </figcaption>
  </figure>

  <h2 class="abs section-head" style="top:732px">WHY ARE COMMUNICATIONS AGENCIES FAILING TO INCREASE THE AA HIRING RATE?</h2>

  <div class="reason reason--1">
    <div class="reason-image" role="img" aria-label="Photo of an industry panel seated on a stage"></div>
    <p class="reason-caption">An industry too inwardly focused to realize that it can be offputting</p>
  </div>
  <div class="reason reason--2">
    <div class="reason-image" role="img" aria-label="Striped illustration of overlapping profiles"></div>
    <p class="reason-caption">Assuming barriers to hiring all people of color are the same and are not unique to each group</p>
  </div>
  <div class="reason reason--3">
    <div class="reason-image" role="img" aria-label="Photo of a graduate holding a sign"></div>
    <p class="reason-caption">Dramatic disconnection from the most critical candidate pool that can provide an immediate &amp; lasting impact</p>
  </div>
  <div class="abs foot-band"></div>
</section>

<section class="page page--back">
  <h1 class="abs mission-title">The Tenfold Mission</h1>
  <div class="abs mission-rule"></div>
  <p class="abs mission-text">Drive parity in opportunity and representation for the most promising young African-American minds while creating a cultural and competitive advantage for progressive communications organizations</p>

  <svg class="flow" width="650" height="520" viewBox="0 0 650 520" fill="none" stroke="#f39200" stroke-width="2">
    <path d="M35 197 H597 Q610 197 610 210 V440 Q610 453 597 453 H48 Q35 453 35 466 V477 Q35 490 48 490 H617"/>
    <g stroke-width="1.6">
      <polyline points="164,191 170,197 164,203"/>
      <polyline points="351,191 357,197 351,203"/>
      <polyline points="604,326 610,332 616,326"/>
      <polyline points="129,447 123,453 129,459"/>
      <polyline points="387,447 381,453 387,459"/>
      <polyline points="297,484 303,490 297,496"/>
    </g>
    <g fill="#f39200" stroke="none">
      <circle cx="100" cy="197" r="6"/><circle cx="242" cy="197" r="6"/><circle cx="460" cy="197" r="6"/>
      <circle cx="164" cy="490" r="6"/><circle cx="470" cy="490" r="6"/>
    </g>
  </svg>

  <div class="step step--connect">
    <h3>Community Connection</h3>
    <p>Tenfold works closely with the African-American communities within relevant college programs with a strong focus on HBCUs</p>
  </div>
  <div class="step step--vetting">
    <h3>Identification &amp; Vetting</h3>
    <p>Candidates are identified through community connection and formally assessed for relevant agency technology skills, emotional, cultural and academic prowess.</p>
  </div>
  <div class="step step--training">
    <h3 style="margin-top:6px">Multi-Focal Training</h3>
    <div class="training-cols">
      <p>Training program specific to advertising industry, to include all major disciplines.</p>
      <p>Coaching provided to crystallize candidate’s personal brand and voice, to improve the communication of value and reduce time spent ‘trying to figure out.’ Coaching also focuses on personal presentation and professional etiquette training to facilitate corporate integration.</p>
    </div>
  </div>
  <div class="step step--onboard">
    <h3>Onboarding Support</h3>
    <p>New hires will be provided innovative e-development platform with personal mentor, to ensure successful onboarding.</p>
  </div>
  <div class="step step--building">
    <h3>Community Building</h3>
    <p>Each Tenfold candidate signs an agreement to initiate a mentoring relationship with a young African American professional hired after them within their organization.</p>
  </div>

  <div class="abs about">
    <h2 class="abs about-title">About Tenfold LLC</h2>
    <div class="abs about-rule"></div>
    <div class="abs about-copy">
      <p>Tenfold is a B Corp (for-profit social enterprise) created by two principles with direct and complimentary experiences in tackling related challenges.</p>
      <p>Jo Marlowe has created a highly successful coaching practice focused on helping soon to graduate, or recently graduated, college students find purpose-driven careers. She is also the founder and Executive Director of the Bridgeway Foundation which provides guidance and assistance for young adults who are “aging out” of the welfare system with over half of the foundation’s fellows being African-American.</p>
      <p>Paul Brennan spent his career in the advertising business culminating in running leading agencies at both Meridian Group and Northline Partners. He has personally dealt with the barriers and frustrations in identifying and attracting talent from the African-American business community despite significant corporate efforts. He has also witnessed the significant advantages gained when truly diversified teams are assembled and nurtured.</p>
    </div>
  </div>
</section>

</body>
</html>
```